Package Label Design Needed for FRUIT JELLY

We need label design for Fruit Jelly Jar and each Fruit Jelly cup(6 flavored cups). Our product is a jar with 6 assorted fruit flavored jellies. (flavors are strawberry, pineapple, mango, lychee, apple, grape) and we need design for :
1) jar label
2) each jelly cup label
All of above (1) & (2) artwork templates and our old labels are attached.
Each jelly is in a heart shaped cup.
Artwork template(dieline) is attached.
Label needs to have followings:
Company logo: Velto (Attached)
Product Name: Brisk Pebbles (Attached) -- TM
Flavor Name: Strawberry or Apple or etc
Old labels are attached to give you an idea. Contents in the old need be pasted in your labels (nutrition facts, net weight etc).
On the label for jar, following phrase must be included:
"Brisk Pebbles TM
with Hidden Treasure Inside"
Coconut Chunk is included inside jelly
Made of Real Fruit Juice
Distributed by Velto, Inc. Marbridge, CA 90417(Back side bottom. Under Nutritional Facts)
Made in Taiwan
(Somewhere in Front)
Low Sugar
0% Transfat
0% Cholesterol
All Natural
Keep refrigerated for an even better taste
Target Market(s)
Both kids and adults who love snacking or who love fun, tasty, fruity snacks.
Industry/Entity Type
Product
Colors
Designer to choose colors to be used in the design.
Requirements
Must have
- Our company logo: Velto
- Product Name: Brisk Pebbles
- ETC

```html
<!DOCTYPE html>
<html lang="en">
<head>
<meta charset="utf-8">
<title>Velto Brisk Pebbles – Cup Labels</title>
<link rel="stylesheet" href="https://fonts.googleapis.com/css2?family=Open+Sans:wght@700;800&display=swap">
<style>
  :root {
    --paper: #ffffff;
    --orange: #ef6c23;
    --orange-dark: #e2601a;
    --sun: #fdc60f;
    --pine-gold: #f2a321;
    --pine-leaf: #3fa535;
    --green: #7fba42;
    --green-light: #a9d160;
    --apple-green: #b5cf5a;
    --apple-red: #d6434f;
    --ink: #1d1d1b;
    --white: #ffffff;
  }
  html, body {
    margin: 0;
    padding: 0;
    width: 886px;
    height: 1200px;
    overflow: hidden;
    background: var(--paper);
  }
  .label-sheet {
    display: block;
    width: 886px;
    height: 1200px;
  }
  .brand-name {
    font-family: "Open Sans", Arial, sans-serif;
    font-weight: 800;
    font-size: 50px;
    fill: var(--ink);
  }
  .product-name {
    font-family: "Open Sans", Arial, sans-serif;
    font-weight: 800;
    font-size: 114px;
    fill: var(--white);
    stroke-width: 6px;
    paint-order: stroke fill;
    stroke-linejoin: round;
    letter-spacing: -2px;
  }
  .product-name--pineapple { stroke: var(--orange); }
  .product-name--apple { stroke: var(--green); }
  .flavor-name {
    font-family: "Open Sans", Arial, sans-serif;
    font-weight: 800;
    fill: var(--white);
  }
  .flavor-name--pineapple { font-size: 30px; }
  .flavor-name--apple { font-size: 44px; }
</style>
</head>
<body>
<svg class="label-sheet" viewBox="0 0 886 1200" xmlns="http://www.w3.org/2000/svg">
  <defs>
    <radialGradient id="pineapple-art" cx="50%" cy="55%" r="60%">
      <stop offset="0%" stop-color="#fbd33a"/>
      <stop offset="55%" stop-color="#f2a321"/>
      <stop offset="100%" stop-color="#3fa535" stop-opacity="0.85"/>
    </radialGradient>
    <radialGradient id="apple-art" cx="50%" cy="60%" r="60%">
      <stop offset="0%" stop-color="#d6434f"/>
      <stop offset="30%" stop-color="#c9b06a"/>
      <stop offset="60%" stop-color="#b5cf5a"/>
      <stop offset="100%" stop-color="#e6efc9"/>
    </radialGradient>
  </defs>

  <!-- Pineapple cup label -->
  <g class="cup-label cup-label--pineapple">
    <path class="label-shape" fill="var(--orange)"
      d="M70,250 C60,200 120,205 180,200 C260,190 300,110 370,60 C430,20 530,15 590,60 C640,100 650,170 700,190 C770,215 815,250 810,330 C805,420 720,520 560,540 C430,555 330,530 240,490 C150,450 65,330 70,250 Z"/>
    <ellipse class="label-glow" cx="480" cy="330" rx="255" ry="165" fill="var(--sun)"/>
    <path class="fruit-art" role="img" aria-label="Illustration of a whole pineapple with leafy crown and a pineapple slice"
      fill="url(#pineapple-art)"
      d="M175,330 C190,250 300,230 360,210 C420,140 520,80 600,110 C660,150 690,230 680,300 C700,360 660,470 560,515 C470,545 330,530 250,480 C200,440 168,390 175,330 Z"/>
    <text class="brand-name" x="470" y="128" text-anchor="middle">Velto</text>
    <text class="product-name product-name--pineapple" x="470" y="277" text-anchor="middle">Brisk</text>
    <text class="product-name product-name--pineapple" x="470" y="403" text-anchor="middle">Pebbles</text>
    <text class="flavor-name flavor-name--pineapple" x="481" y="499" text-anchor="middle">Pineapple</text>
  </g>

  <!-- Apple cup label -->
  <g class="cup-label cup-label--apple">
    <path class="label-shape" fill="var(--green)" stroke="var(--ink)" stroke-width="1"
      d="M85,860 C80,820 110,800 170,790 C240,780 280,720 340,680 C410,640 520,640 580,665 C640,690 640,740 690,770 C770,810 840,860 830,950 C820,1050 740,1140 560,1155 C400,1165 250,1150 160,1080 C110,1040 90,920 85,860 Z"/>
    <ellipse class="label-glow" cx="470" cy="760" rx="110" ry="70" fill="var(--green-light)" opacity="0.6"/>
    <path class="fruit-art" role="img" aria-label="Photo of green apples in a row with a red apple in front"
      fill="url(#apple-art)"
      d="M170,900 C175,860 230,850 290,858 C350,830 430,840 470,860 C540,840 640,840 700,860 C760,850 795,880 790,940 C785,1000 740,1030 680,1040 C640,1100 600,1140 520,1150 C440,1158 400,1120 380,1080 C300,1060 220,1030 185,1010 C165,970 165,930 170,900 Z"/>
    <text class="brand-name" x="476" y="758" text-anchor="middle">Velto</text>
    <text class="product-name product-name--apple" x="480" y="905" text-anchor="middle">Brisk</text>
    <text class="product-name product-name--apple" x="480" y="1031" text-anchor="middle">Pebbles</text>
    <text class="flavor-name flavor-name--apple" x="485" y="1110" text-anchor="middle">Apple</text>
  </g>
</svg>
</body>
</html>
```